Hero Image Creation for Duchess of Thread (DOT)

Current Site - https://duchessofthread.com.au/
Project: Create 6 high-resolution hero banner images for the Duchess of Thread website to suit the Hero Banner Image of Cartwell
Style: Clean, modern, premium, bright, minimal, white background
1. Marlowe Fabrics Hero Image (Priority #1)
Goal: Showcase Marlowe tana lawn quilting fabrics in a beautiful, premium style. What to include: A mix of Marlowe floral quilting fabrics
Clean white background
Soft, natural lighting
Balanced, aesthetically pleasing composition
Feminine, delicate, elegant feel
Text overlay (must be exactly as below):
H1: Be Inspired to Create
Subheading: Discover Australia's Most Beautiful Range of Marlowe Quilting Fabrics
CTA Button: Shop Marlowe
2–6. Additional Hero Images (to be created after the Marlowe image)
Designers must create banners in a consistent visual style using the same dimensions and white background.
Themes:
Vela Rose Feature Collection
Quilting Fabrics Overview
Fabric Bundles & Curated Packs
Upcycled / Clearance / End-of-Bolt Fabrics
Classes / Creative Community (for 2026)
(Each will have its own text, but the visual brand style must remain cohesive.)
Brand Guidelines:
Clean, premium, modern aesthetic
White, airy background
Pastel tones and floral designs are preferred
Fonts similar to elegant script + clean sans serif (designer may propose alternatives)
Must feel warm, inspiring, and feminine
Avoid clutter — minimalistic but inviting
Deliverables:
6 final hero images in 2048 × 1024 px, highest resolution for Cartwell website
1 editable source file per image (PSD, AI, or layered file)
Ensure text remains readable on desktop and mobile versions
Ensure fabric prints look clear and high-quality
Fabric photos (Marlowe, Vela Rose, etc.)
Brand colours & fonts
# 7 D 8 8 6 E
# A 3 B E A F
# B 4 B 1 C 6
# C 5 A 8 A A
# E B E 5 E2
Bebas Neue Headings
Questrial Body
Overall Objective:
To create a set of visually cohesive hero banners that instantly communicate what Duchess of Thread sells, highlighting:
Marlowe Fabrics
Vela Rose
Bundles
Clearance/upcycled items
Community and classes
The final images must help customers immediately understand what DOT offers and feel inspired to shop.

```html
<!DOCTYPE html>
<html lang="en">
<head>
<meta charset="utf-8">
<title>Duchess of Thread – Hero Banners</title>
<link rel="stylesheet" href="https://fonts.googleapis.com/css2?family=Questrial&display=swap">
<style>
  :root {
    --stage: #3d3e3d;
    --pink: #fb6cc1;
    --pink-deep: #f45fb4;
    --green: #a3d48a;
    --green-soft: #9fd08a;
    --white: #ffffff;
    --patch-rose: #c43a5c;
    --patch-navy: #24355e;
    --patch-gold: #e2a72c;
    --patch-teal: #3f7fa8;
    --floral-cream: #efe7e0;
    --floral-violet: #7b5cb5;
    --floral-lilac: #9b82c9;
    --floral-orange: #eba15b;
  }
  * { box-sizing: border-box; margin: 0; padding: 0; }
  html, body { width: 1112px; height: 1200px; overflow: hidden; }
  body {
    background: var(--stage);
    font-family: "Questrial", sans-serif;
    color: var(--white);
    position: relative;
  }
  .banner {
    position: absolute;
    left: 70px;
    width: 970px;
    height: 485px;
    overflow: hidden;
  }
  .banner--centered { top: 84px; }
  .banner--split { top: 646px; background: var(--green); }

  /* Patchwork banner */
  .patchwork {
    position: absolute; inset: 0;
    background:
      radial-gradient(circle at 12% 22%, var(--patch-rose) 0 10%, transparent 30%),
      radial-gradient(circle at 88% 75%, var(--patch-gold) 0 8%, transparent 28%),
      radial-gradient(circle at 80% 18%, var(--patch-teal) 0 8%, transparent 26%),
      radial-gradient(circle at 20% 85%, var(--patch-gold) 0 6%, transparent 24%),
      linear-gradient(135deg, var(--patch-navy), #8b2a55 40%, #c9573a 70%, var(--patch-navy));
  }
  .feature-card {
    position: absolute;
    left: 242px; top: 83px;
    width: 488px; height: 319px;
    background: var(--pink);
    border: 2px solid var(--green);
    border-radius: 26px;
    text-align: center;
  }
  .brand-name {
    position: absolute;
    left: 0; right: 0; top: 66px;
    font-size: 17px;
    letter-spacing: 0.5px;
  }
  .brand-name::before {
    content: "";
    display: inline-block;
    width: 8px; height: 8px;
    border-radius: 50%;
    background: var(--white);
    margin-right: 8px;
    vertical-align: middle;
  }
  .feature-card h1 {
    position: absolute; left: 0; right: 0; top: 133px;
    font-weight: 400;
    font-size: 39px;
    line-height: 35px;
    text-shadow: 0 2px 3px rgba(0,0,0,0.25);
  }
  .feature-card p {
    position: absolute; left: 0; right: 0; top: 210px;
    font-size: 13.6px;
    line-height: 19.5px;
  }
  .btn {
    position: absolute;
    display: flex; align-items: center; justify-content: center;
    border-radius: 999px;
    color: var(--white);
    text-decoration: none;
    box-shadow: 0 2px 4px rgba(0,0,0,0.2);
  }
  .btn--green {
    left: 189px; top: 262px;
    width: 96px; height: 26px;
    background: var(--green-soft);
    font-size: 9.5px;
  }

  /* Split banner */
  .floral-field { position: absolute; inset: 0; }
  .split-copy {
    position: absolute;
    top: 0; bottom: 0; right: 45px;
    width: 900px;
    text-align: right;
  }
  .split-copy h1 {
    position: absolute; right: 0; top: 38px;
    width: 600px;
    font-weight: 400;
    font-size: 70px;
    line-height: 66px;
    text-shadow: 0 2px 4px rgba(0,0,0,0.2);
  }
  .split-copy p {
    position: absolute; right: 0; top: 313px;
    width: 560px;
    font-size: 21.5px;
    line-height: 32px;
  }
  .btn--pink {
    right: 0; top: 396px;
    width: 147px; height: 43px;
    background: var(--pink-deep);
    font-size: 16.5px;
  }
</style>
</head>
<body>
  <section class="banner banner--centered">
    <div class="patchwork" role="img" aria-label="Patchwork quilt of colourful floral fabric squares"></div>
    <div class="feature-card">
      <div class="brand-name">Duchess of Thread</div>
      <h1>BE INSPIRED TO<br>CREATE</h1>
      <p>Discover Australia's Most Beautiful Range of<br>Marlowe Quilting Fabrics</p>
      <a class="btn btn--green" href="#">Shop Marlowe</a>
    </div>
  </section>

  <section class="banner banner--split">
    <svg class="floral-field" width="970" height="485" viewBox="0 0 970 485" role="img" aria-label="Floral fabric print with violet and orange flowers on cream, torn edge">
      <defs>
        <linearGradient id="floralTone" x1="0" y1="0" x2="1" y2="1">
          <stop offset="0" stop-color="var(--floral-cream)"/>
          <stop offset="0.45" stop-color="var(--floral-violet)"/>
          <stop offset="0.8" stop-color="var(--floral-lilac)"/>
          <stop offset="1" stop-color="var(--floral-orange)"/>
        </linearGradient>
      </defs>
      <path fill="url(#floralTone)" d="M0 0 H590 L583 30 L595 60 L588 95 L600 130 L592 165 L605 195 L590 225 L575 250 L545 265 L520 275 L495 285 L475 300 L462 330 L455 360 L445 395 L430 430 L418 460 L405 485 H0 Z"/>
    </svg>
    <div class="split-copy">
      <h1>BE<br>INSPIRED<br>TO<br>CREATE</h1>
      <p>Discover Australia's Most Beautiful Range<br>of Marlowe Quilting Fabrics</p>
      <a class="btn btn--pink" href="#">Shop Marlowe</a>
    </div>
  </section>
</body>
</html>
```